OrvenPharmacy brochure

Need a brochure design for an easy step guid about and how to order from OrvenPharmacy. We would like it very attractive but also clear to read as it is mainly targeting elderly. Attached is 2 alternate logos u can use and the information we would like the brochure to contain

```html
<!DOCTYPE html>
<html lang="en">
<head>
<meta charset="utf-8">
<title>OrvenPharmacy – Rural Medication Service Brochure</title>
<link href="https://fonts.googleapis.com/css2?family=Source+Sans+3:ital,wght@0,400;0,600;0,700;1,400;1,700&family=PT+Sans+Narrow:wght@400;700&display=swap" rel="stylesheet">
<style>
:root{
  --brand-red:#c41a30;
  --charcoal:#3a3a3c;
  --navy:#1d2d3d;
  --sky:#2fa3dc;
  --bullet:#f4b43e;
  --white:#ffffff;
  --ink:#2b2b2b;
  --page:#ffffff;
}
*{box-sizing:border-box;margin:0;padding:0}
html,body{width:1200px;height:1000px;overflow:hidden;background:var(--page)}
body{font-family:"Source Sans 3",Arial,sans-serif;position:relative}
.brochure{position:absolute;left:24px;top:73px;width:1148px;height:812px;display:flex}
.panel{position:relative;width:383px;height:100%}
.panel--faq{background:var(--brand-red);color:var(--white)}
.panel--contact{background:var(--white);width:382px}
.panel--cover{background:var(--brand-red);color:var(--white)}

/* FAQ panel */
.faq-header{position:absolute;left:0;top:20px;width:383px;height:42px;background:var(--charcoal);display:flex;align-items:center;padding-left:28px;gap:8px}
.faq-header h2{font-size:19px;font-weight:600}
.faq-icon{width:30px;height:30px}
.faq-list{position:absolute;left:34px;top:82px;width:322px;list-style:none}
.faq-item{position:relative;padding-left:16px;margin-bottom:24px}
.faq-item::before{content:"";position:absolute;left:0;top:8px;width:7px;height:7px;border-radius:50%;background:var(--bullet)}
.faq-q{font-size:16px;font-weight:600;line-height:20px;margin-bottom:4px}
.faq-a{font-size:13px;font-style:italic;line-height:16.5px}
.faq-a--spaced{margin-top:16px}
.faq-a strong{font-weight:700}
.help-pill{position:absolute;left:19px;top:452px;width:344px;height:24px;border:1.5px solid var(--white);border-radius:12px;background:var(--charcoal);font-size:13px;font-weight:600;text-align:center;line-height:21px}
.help-number{position:absolute;left:0;top:484px;width:383px;text-align:center;font-family:"PT Sans Narrow",sans-serif;font-weight:700;font-size:30px}
.photo{position:absolute}
.photo--landscape{left:19px;top:562px;width:344px;height:230px;background:linear-gradient(180deg,#7fb3cf 0%,#a9cfe0 38%,#c9a66a 58%,#a58a52 82%,#6f7a45 100%)}

/* Name lockups */
.brand-mark{display:flex;align-items:center;gap:6px}
.brand-mark__dot{width:11px;height:11px;border-radius:50%;background:var(--brand-red)}
.brand-mark__name{font-weight:600;font-size:17px;color:var(--brand-red)}
.brand-tagline{font-size:8.5px;color:var(--brand-red);margin-left:17px;margin-top:1px}

/* Contact panel */
.contact-block{position:absolute;left:114px;top:574px}
.contact-list{list-style:none;margin-top:26px;margin-left:8px;font-family:"PT Sans Narrow",sans-serif;font-size:13px;color:var(--ink)}
.contact-list li{display:flex;align-items:flex-start;gap:10px;margin-bottom:8px;line-height:18px}
.contact-list svg{width:18px;height:18px;flex:none}

/* Cover panel */
.cover-brand{position:absolute;left:40px;top:56px}
.cover-brand .brand-mark{gap:10px}
.cover-brand .brand-mark__name{color:var(--white);font-size:32px}
.cover-brand .brand-mark__dot{background:var(--white);width:16px;height:16px}
.cover-brand .brand-tagline{color:var(--white);font-size:16px;margin-left:26px;margin-top:2px}
.cover-rule{position:absolute;left:0;top:157px;width:383px;height:4px;background:var(--sky)}
.photo--doctor{left:0;top:161px;width:383px;height:434px;background:linear-gradient(120deg,#b9c2c9 0%,#e2e6e9 45%,#f3f3f1 70%,#d6dde2 100%)}
.cover-title{position:absolute;left:33px;top:614px;font-size:32px;font-weight:700;line-height:39px;letter-spacing:.5px}
.url-bar{position:absolute;left:0;top:772px;width:383px;height:2px;background:var(--navy)}
.url-pill{position:absolute;left:83px;top:763px;width:216px;height:21px;border-radius:11px;background:var(--navy);color:var(--white);font-size:13px;letter-spacing:1.6px;text-align:center;line-height:21px}
</style>
</head>
<body>
<main class="brochure">

  <section class="panel panel--faq">
    <header class="faq-header">
      <svg class="faq-icon" viewBox="0 0 30 30"><circle cx="15" cy="15" r="13" fill="#c41a30" stroke="#fff" stroke-width="2"/><text x="15" y="21" text-anchor="middle" font-family="Source Sans 3, sans-serif" font-weight="700" font-size="18" fill="#fff">?</text></svg>
      <h2>Commonly Asked Questions?</h2>
    </header>
    <ul class="faq-list">
      <li class="faq-item">
        <p class="faq-q">Who are we?</p>
        <p class="faq-a">Group of Pharmacists with over 20 years experience in Rural Pharmacy. No Big Corporations, we understand the service rural customers want.</p>
      </li>
      <li class="faq-item">
        <p class="faq-q">Where are we?</p>
        <p class="faq-a">Your orders are prepared and sent to you from Hartwell &amp; Eden Ridge Pharmacies, located in <strong>Marlow Hills, South Australia</strong></p>
      </li>
      <li class="faq-item">
        <p class="faq-q">What happens to your prescription when you send it to us?</p>
        <p class="faq-a faq-a--spaced">When you send us your prescription in the mail or through your OP depot, once we receive it we attach your new repeats and post straight back to you. If you would like to take advantage of our prescription filing system you can notify us anytime.</p>
      </li>
    </ul>
    <p class="help-pill">Any Questions about this Service call us on:</p>
    <p class="help-number">1300 482 730</p>
    <div class="photo photo--landscape" role="img" aria-label="Rural landscape with a gum tree in a dry grassy paddock under a blue sky"></div>
  </section>

  <section class="panel panel--contact">
    <div class="contact-block">
      <div class="brand-mark"><span class="brand-mark__dot"></span><span class="brand-mark__name">OrvenPharmacy</span></div>
      <p class="brand-tagline">Caring for country communities</p>
      <ul class="contact-list">
        <li><svg viewBox="0 0 18 18"><path d="M2 9 9 3l7 6M4 8v7h4v-4h2v4h4V8" fill="none" stroke="#c41a30" stroke-width="2"/></svg><span>PO Box 742<br>Hartwell SA 5291</span></li>
        <li><svg viewBox="0 0 18 18"><path d="M5 2c-2 1-3 3-1 7s5 7 8 7c1 0 2-1 2-2l-3-2-2 1c-1-1-3-3-3-5l1-2-2-4z" fill="#c41a30"/></svg><span>P: 1300 482 730</span></li>
        <li><svg viewBox="0 0 18 18"><rect x="5" y="2" width="8" height="4" fill="none" stroke="#c41a30" stroke-width="1.6"/><rect x="2" y="6" width="14" height="7" rx="1" fill="none" stroke="#c41a30" stroke-width="1.6"/><rect x="5" y="11" width="8" height="5" fill="#fff" stroke="#c41a30" stroke-width="1.6"/></svg><span>F: 08 8634 1187</span></li>
        <li><svg viewBox="0 0 18 18"><rect x="2" y="4" width="14" height="10" fill="none" stroke="#c41a30" stroke-width="1.6"/><path d="M2 4l7 6 7-6" fill="none" stroke="#c41a30" stroke-width="1.6"/></svg><span>sales@orvenpharmacy.com.au</span></li>
        <li><svg viewBox="0 0 18 18"><circle cx="9" cy="9" r="7" fill="none" stroke="#c41a30" stroke-width="1.6"/><ellipse cx="9" cy="9" rx="3" ry="7" fill="none" stroke="#c41a30" stroke-width="1.4"/><path d="M2 9h14" stroke="#c41a30" stroke-width="1.4"/></svg><span>www.orvenpharmacy.com.au</span></li>
      </ul>
    </div>
  </section>

  <section class="panel panel--cover">
    <div class="cover-brand">
      <div class="brand-mark"><span class="brand-mark__dot"></span><span class="brand-mark__name">OrvenPharmacy</span></div>
      <p class="brand-tagline">Caring for country communities</p>
    </div>
    <div class="cover-rule"></div>
    <div class="photo photo--doctor" role="img" aria-label="Close-up of a doctor's hand holding out a stethoscope toward the viewer"></div>
    <h1 class="cover-title">RURAL<br>MEDICATION<br>SERVICE</h1>
    <div class="url-bar"></div>
    <p class="url-pill">www.orvenpharmacy.com.au</p>
  </section>

</main>
</body>
</html>
```